Private Learning Centre in Singapore needs a flyer design

We need a flyer design for our upcoming education fair and also able to use it for day to day purpose. The aim is to attract parents, students to enrol for classes by offering them free trial class/assessment. 2 sided flyer with the front page as the logo only and details on the other page. We would like to see a final design in blue, white and it should be curious and attractive enough not to allow customers to throw it away once they received it.

Education

```html
<!DOCTYPE html>
<html lang="en">
<head>
<meta charset="utf-8">
<title>Free Trial Class Flyer – Bright Path Academy</title>
<link rel="stylesheet" href="https://fonts.googleapis.com/css2?family=Alfa+Slab+One&family=Open+Sans:wght@400;700&display=swap">
<style>
  :root {
    --page-bg: #e9e9ec;
    --chalk-dark: #1f2124;
    --chalk-mid: #3a3d42;
    --chalk-white: #f2f2f2;
    --chalk-blue: #55b8ea;
    --chalk-yellow: #efe77a;
    --navy: #0d2a5c;
    --navy-deep: #0a1f47;
    --sky: #1ea0e0;
    --sky-light: #4cc0f2;
    --accent-text: #33b5ef;
    --white: #ffffff;
  }
  * { box-sizing: border-box; margin: 0; padding: 0; }
  html, body {
    width: 902px; height: 1200px; overflow: hidden;
    background: var(--page-bg);
    font-family: "Open Sans", Arial, sans-serif;
  }
  .flyer {
    position: absolute; left: 75px; top: 42px;
    width: 783px; height: 1103px;
    overflow: hidden;
    box-shadow: 0 6px 18px rgba(0,0,0,.25);
    background: var(--chalk-dark);
  }
  .flyer__art { position: absolute; inset: 0; }
  .social { position: absolute; top: 42px; right: 24px; display: flex; gap: 20px; }
  .social__dot { width: 34px; height: 34px; border-radius: 50%; background: var(--white); }
  .headline {
    position: absolute; left: 0; right: 0; top: 52px;
    text-align: center;
    font-family: "Alfa Slab One", Georgia, serif;
    line-height: 1;
    letter-spacing: 4px;
  }
  .headline span { display: block; }
  .headline__free { font-size: 92px; color: var(--chalk-white); }
  .headline__trial { font-size: 100px; color: var(--chalk-blue); margin-top: 8px; }
  .headline__class { font-size: 132px; color: var(--chalk-yellow); margin-top: 10px; }
  .brand-mark {
    position: absolute; left: 600px; top: 740px; width: 170px;
    display: flex; flex-direction: column; align-items: center; gap: 10px;
  }
  .brand-mark__dot { width: 56px; height: 56px; border-radius: 50%; background: var(--sky); }
  .brand-mark__name { color: var(--sky-light); font-size: 15px; font-weight: 400; letter-spacing: 2px; text-transform: uppercase; text-align: center; }
  .about {
    position: absolute; right: 30px; top: 866px; width: 420px;
    text-align: right; color: var(--white);
    font-size: 16.5px; line-height: 23.5px;
  }
  .about strong { color: var(--accent-text); font-weight: 700; }
  .contact { position: absolute; left: 43px; top: 946px; color: var(--white); }
  .contact__name { color: var(--navy); font-weight: 700; font-size: 18.5px; letter-spacing: .3px; margin-bottom: 12px; }
  .contact__list { list-style: none; font-size: 16px; }
  .contact__list li { display: flex; align-items: center; gap: 12px; height: 29px; }
  .contact__list svg { width: 16px; height: 16px; fill: var(--navy); flex: none; }
</style>
</head>
<body>
<main class="flyer">
  <svg class="flyer__art" viewBox="0 0 783 1103" width="783" height="1103">
    <defs>
      <radialGradient id="chalkboard" cx="55%" cy="40%" r="75%">
        <stop offset="0" stop-color="#45484d"/>
        <stop offset="1" stop-color="#1c1e21"/>
      </radialGradient>
      <linearGradient id="supplies" x1="0" y1="1" x2="1" y2="0">
        <stop offset="0" stop-color="#8a4fc4" stop-opacity=".55"/>
        <stop offset=".4" stop-color="#f08a2a" stop-opacity=".45"/>
        <stop offset=".7" stop-color="#d8e640" stop-opacity=".45"/>
        <stop offset="1" stop-color="#e040b0" stop-opacity=".5"/>
      </linearGradient>
      <linearGradient id="navyPanel" x1="0" y1="0" x2="1" y2="1">
        <stop offset="0" stop-color="#1a4a8c"/>
        <stop offset="1" stop-color="var(--navy-deep)"/>
      </linearGradient>
      <linearGradient id="skyPanel" x1="0" y1="0" x2="1" y2="1">
        <stop offset="0" stop-color="#2bb3f0"/>
        <stop offset="1" stop-color="#1592d6"/>
      </linearGradient>
    </defs>
    <rect width="783" height="1103" fill="url(#chalkboard)" role="img" aria-label="Chalkboard background"/>
    <path d="M0 780 L0 660 C120 600 300 560 450 500 C560 450 680 420 783 380 L783 640 Z" fill="url(#supplies)" role="img" aria-label="Photo of colourful school supplies: alphabet letters, pencils, highlighters, scissors, notebook and calculator on a chalkboard"/>
    <polygon points="-10,932 783,632 783,1103 -10,1103" fill="var(--white)"/>
    <polygon points="300,832 783,642 783,1103 388,1103" fill="url(#navyPanel)"/>
    <polygon points="0,928 296,826 382,1103 0,1103" fill="url(#skyPanel)"/>
  </svg>

  <div class="social" aria-hidden="true">
    <span class="social__dot"></span>
    <span class="social__dot"></span>
  </div>

  <h1 class="headline">
    <span class="headline__free">FREE</span>
    <span class="headline__trial">TRIAL</span>
    <span class="headline__class">CLASS</span>
  </h1>

  <div class="brand-mark">
    <span class="brand-mark__dot"></span>
    <span class="brand-mark__name">Bright Path Academy</span>
  </div>

  <p class="about">
    Bright Path Academy<br>
    is where you can develop<br>
    academic and life skills. Our teachers<br>
    are the heartbeat of the business. They inspire<br>
    and nurture students, helping them surpass<br>
    their expectations. We cover<br>
    <strong>English, Mathematics and Science</strong> from<br>
    <strong>Primary and Secondary Levels</strong>
  </p>

  <section class="contact">
    <h2 class="contact__name">BRIGHT PATH ACADEMY</h2>
    <ul class="contact__list">
      <li><svg viewBox="0 0 24 24"><path d="M6.6 10.8a15 15 0 0 0 6.6 6.6l2.2-2.2c.3-.3.7-.4 1-.2 1.1.4 2.3.6 3.6.6.6 0 1 .4 1 1V20c0 .6-.4 1-1 1A17 17 0 0 1 3 4c0-.6.4-1 1-1h3.5c.6 0 1 .4 1 1 0 1.3.2 2.5.6 3.6.1.3 0 .7-.2 1z"/></svg>6123 4567</li>
      <li><svg viewBox="0 0 24 24"><path d="M2 5h20v14H2z M2 5l10 8 10-8" fill="none" stroke="var(--navy)" stroke-width="2"/></svg>enquire@brightpathacademy.com</li>
      <li><svg viewBox="0 0 24 24"><path d="M12 3 2 12h3v9h5v-6h4v6h5v-9h3z"/></svg>18 Seaview Lane S400123</li>
    </ul>
  </section>
</main>
</body>
</html>
```